Foundation repair and service company needs website

*All Submissions must have a Homepage and related Subpage concept*
Wordpress design requires that you provide the template or framework used to design the concept.

Wordpress design for a residential (50%) and commercial (50%) foundation repair and service company. The site should be clean and professional looking. Client provides services statewide in Texas, Louisiana, Kansas and Missouri. Commercial services are offered all across the U.S. with over 35 years in the business.

Site should be clean and professional.

Search Engine Optimization (SEO) is also a concern so we need to make sure to have several sections for text on the home page. We also want to have some areas for clear calls to action (example: download a free information packet)

Logo usage should be the Stonebrace "ARM" with transparent background and red lettering. (attached)

Current website
http://stonebracefooting.example/

Competition:

Residential
www.keystayslabworks.example
http://www.verdicebase.example/
http://www.pilgrove.example/

Commercial
http://www.tovesa.example/
http://www.groundlinkgoods.example/FOUNDATION_REPAIR.asp

We have attached a design document with more information directly from the client, please review that prior to designing.
Updates

Client provided site they like :

http://www.brukvelt.example/en/USA/

uploaded 2 new images from client. 

Industry/Entity Type

Residential

Requirements
Must have
• 1. easy to read fonts
2. image slider / banner
3. request a quote form
4. Download information packet
5. social media: FB, Twitter,
6 SEO friendly footer for nav links , keywords, social, contact info
7. concept must use client phone numbers and contact info
(lorum ipsom is OK for content areas but using actual client content will increase the chance of you design being selected as the winner.

Should not have
• do not use red,white. blue theme
do not place a search site bar on the concept

```html
<!DOCTYPE html>
<html lang="en">
<head>
<meta charset="utf-8">
<title>Stonebrace Foundation Repair</title>
<link href="https://fonts.googleapis.com/css2?family=Titillium+Web:wght@300;400;600;700&family=Open+Sans:wght@400;600;700&display=swap" rel="stylesheet">
<style>
:root{
  --red:#c8161d;
  --red-dark:#a80f15;
  --ink:#1d1d1d;
  --header:#1a1a1a;
  --footer:#232323;
  --page:#efefef;
  --muted:#7a7a7a;
  --footer-text:#b9b9b9;
  --green:#5fb51f;
  --green-dark:#3f8f0f;
}
*{box-sizing:border-box;margin:0;padding:0}
html,body{width:826px;height:1200px;overflow:hidden}
body{position:relative;background:var(--page);font-family:"Open Sans",Arial,sans-serif;color:var(--ink)}
.abs{position:absolute}

/* header */
.site-header{left:0;top:0;width:826px;height:66px;background:var(--header);z-index:3}
.brand{left:75px;top:0;width:134px;height:75px;background:linear-gradient(#fff,#e8e8e8);border-radius:0 0 3px 3px;box-shadow:0 1px 3px rgba(0,0,0,.4);z-index:4;display:flex;align-items:center;justify-content:center;font-family:"Titillium Web",sans-serif;font-weight:700;font-size:19px;color:var(--red)}
.utility{top:4px;right:86px;font-size:9.5px;color:#fff;display:flex;gap:12px;z-index:4}
.main-nav{top:38px;left:288px;display:flex;gap:0;z-index:4}
.main-nav a{font-size:9.6px;color:#fff;text-decoration:none;padding:3px 8px;line-height:12px;margin-right:2px}
.main-nav a.active{background:var(--red);border-radius:2px}

/* hero */
.hero{left:0;top:66px;width:826px;height:339px;background:linear-gradient(180deg,#6d6a62 0%,#8a7d5e 40%,#5a5648 75%,#8d8d8f 100%)}
.hero-title{left:70px;top:172px;width:182px;height:72px;background:rgba(0,0,0,.88);border-left:3px solid #111;padding:10px 0 0 12px;font-family:"Titillium Web",sans-serif;color:#fff;font-weight:300;font-size:20px;line-height:25px}
.hero-title strong{font-weight:600}
.hero-cta{left:0;top:249px;width:270px;height:42px;background:rgba(0,0,0,.88);color:#fff;font-family:"Titillium Web",sans-serif;font-weight:600;font-size:13.5px;line-height:42px;padding-left:82px}
.hero-cta-arrow{left:262px;top:249px}
.hero-next{left:750px;top:212px}

/* band */
.promo-band{left:0;top:405px;width:826px;height:48px;background:linear-gradient(var(--red),var(--red-dark))}
.promo-band h2{position:absolute;left:80px;top:6px;font-family:"Titillium Web",sans-serif;font-weight:600;font-size:16px;color:#fff}
.promo-band p{position:absolute;left:80px;top:27px;font-family:"Titillium Web",sans-serif;font-weight:600;font-size:12.5px;color:#fff}
.dots{left:415px;top:425px;display:flex;gap:2px}
.dots span{width:7px;height:7px;border-radius:50%;background:#111}
.dots span.on{background:#fff}
.phone-box{left:599px;top:417px;width:136px;height:24px;background:#f5f5f5;border-radius:2px;font-family:"Titillium Web",sans-serif;font-size:15px;color:#333;text-align:center;line-height:24px}
.band-notch{left:426px;top:453px}

/* services */
.service{top:485px;width:210px}
.service .photo{width:210px;height:116px}
.service h3{margin:14px 0 0 2px;font-family:"Titillium Web",sans-serif;font-weight:600;font-size:11px;color:#222}
.service p{margin:4px 0 0 2px;font-size:8px;line-height:13px;color:var(--muted)}

/* video panel */
.video-panel{left:76px;top:692px;width:676px;height:282px;background:#fff;border:1px solid #e3e3e3}
.video-panel h2{position:absolute;left:14px;top:17px;font-family:"Titillium Web",sans-serif;font-weight:600;font-size:18px;color:#222}
.rule{position:absolute;left:123px;top:31px;width:496px;border-top:3px dotted #ddd}
.pager{position:absolute;top:26px;width:14px;height:14px;background:#ddd;color:#fff;font-size:9px;text-align:center;line-height:14px}
.player{position:absolute;left:14px;top:57px;width:407px;height:199px;background:linear-gradient(#8f9294,#7a776c 60%,#6b665d);box-shadow:0 10px 12px -8px rgba(0,0,0,.45)}
.player-bar{position:absolute;left:0;bottom:0;width:407px;height:20px;background:rgba(0,0,0,.65)}
.player-side{position:absolute;left:368px;width:25px;height:20px;background:rgba(0,0,0,.75);border-radius:2px}
.quote-form{position:absolute;left:433px;top:57px;width:227px;height:195px;background:#e8e8e8;border:1px solid #d3d3d3;border-radius:2px}
.field{position:absolute;left:10px;width:206px;background:#fff;border:1px solid #bdbdbd;font-family:Arial,sans-serif;font-weight:700;font-size:9px;color:#555;padding:7px 8px}
.send{position:absolute;left:31px;top:177px;width:150px;height:28px;border-radius:14px;background:linear-gradient(#8bd33f,var(--green) 55%,var(--green-dark));color:#fff;font-family:Arial,sans-serif;font-weight:700;font-size:10.5px;text-align:center;line-height:28px}

/* footer */
.site-footer{left:0;top:996px;width:826px;height:204px;background:var(--footer)}
.footer-col{position:absolute;top:13px}
.footer-col h4{width:100px;text-align:center;border-top:1px solid #555;border-bottom:1px solid #555;padding:4px 0 5px;font-family:"Titillium Web",sans-serif;font-weight:600;font-size:12px;color:#fff;position:relative}
.footer-col h4::after{content:"";position:absolute;left:38px;bottom:-1px;width:24px;height:1px;background:var(--red)}
.footer-col ul{list-style:none;margin-top:15px}
.footer-col li,.footer-col p{font-size:8.5px;line-height:14px;color:var(--footer-text)}
.copyright{left:87px;top:1173px;font-size:7.5px;color:#aaa;font-family:Arial,sans-serif}
.social{left:612px;top:1168px;display:flex;gap:6px}
.social span{width:16px;height:16px;border-radius:3px}
</style>
</head>
<body>

<header class="abs site-header"></header>
<div class="abs brand">Stonebrace</div>
<div class="abs utility"><span>Support</span><span>Login</span></div>
<nav class="abs main-nav">
  <a class="active">HOME</a><a>ABOUT US</a><a>RESIDENTIAL</a><a>COMMERCIAL</a><a>FAQ</a><a>CONTACT US</a><a>DEALERSHIPS</a>
</nav>

<section class="abs hero" role="img" aria-label="Industrial foundation repair site with machinery and ductwork"></section>
<div class="abs hero-title">Our Reputation is<br><strong>Rock Solid</strong></div>
<div class="abs hero-cta">Download Information Packet</div>
<svg class="abs hero-cta-arrow" width="36" height="42" viewBox="0 0 36 42"><polygon points="12,0 36,0 24,42 0,42" fill="var(--red)"/><polyline points="16,16 21,21 16,26" fill="none" stroke="#fff" stroke-width="1.6"/></svg>
<svg class="abs hero-next" width="16" height="32" viewBox="0 0 16 32"><polyline points="2,2 14,16 2,30" fill="none" stroke="#ccc" stroke-width="4"/></svg>

<section class="abs promo-band">
  <h2>State of the art technology</h2>
  <p>Services Across the nation</p>
</section>
<div class="abs dots"><span class="on"></span><span></span><span></span><span></span></div>
<div class="abs phone-box">1-800-555-0142</div>
<svg class="abs band-notch" width="14" height="7" viewBox="0 0 14 7"><polygon points="0,0 14,0 7,7" fill="var(--red-dark)"/></svg>

<article class="abs service" style="left:76px">
  <div class="photo" role="img" aria-label="Crew inspecting steel beam lifting equipment" style="background:linear-gradient(#b5b9bd,#6c7077)"></div>
  <h3>About Us</h3>
  <p>Stonebrace is one of the largest underpinning compa-nies in the business. We have been in the structural repair field for more than 35 years.</p>
</article>
<article class="abs service" style="left:309px">
  <div class="photo" role="img" aria-label="Technician greeting a homeowner beside a service truck" style="background:linear-gradient(#8d8677,#4f4a43 60%,#9b3a35)"></div>
  <h3>Residential</h3>
  <p>Stonebrace is one of the largest companies in the business. Our residential services are offered state-wide in Texas, Louisiana, Kansas, and Missouri.</p>
</article>
<article class="abs service" style="left:541px">
  <div class="photo" role="img" aria-label="Engineers reviewing plans at a commercial construction site" style="background:linear-gradient(#9ec7ea,#d9e6ee 55%,#b9a65a)"></div>
  <h3>Commercial</h3>
  <p>Stonebrace is one of the largest companies in the business. Our residential services are offered state-wide in Texas, Louisiana, Kansas, and Missouri.</p>
</article>

<section class="abs video-panel">
  <h2>Our Video</h2>
  <div class="rule"></div>
  <div class="pager" style="left:632px">‹</div>
  <div class="pager" style="left:649px">›</div>
  <div class="player" role="img" aria-label="Video of excavator working at a foundation repair site">
    <svg style="position:absolute;left:187px;top:78px" width="38" height="38" viewBox="0 0 38 38"><circle cx="19" cy="19" r="19" fill="#111"/><polygon points="15,11 27,19 15,27" fill="#fff"/></svg>
    <div class="player-side" style="top:19px"></div>
    <div class="player-side" style="top:41px"></div>
    <div class="player-side" style="top:63px"></div>
    <div class="player-side" style="top:85px"></div>
    <div class="player-bar">
      <svg style="position:absolute;left:7px;top:2px" width="30" height="16" viewBox="0 0 30 16"><rect width="30" height="16" fill="#222"/><polygon points="12,4 20,8 12,12" fill="#fff"/></svg>
      <div style="position:absolute;left:47px;top:8px;width:290px;height:4px;background:#222"><div style="width:48px;height:4px;background:#1a9be0"></div></div>
      <div style="position:absolute;left:344px;top:5px;font:700 italic 8px Arial,sans-serif;color:#1a9be0">||||| HD</div>
    </div>
  </div>
  <form class="quote-form">
    <div class="field" style="top:11px;height:23px">Name</div>
    <div class="field" style="top:40px;height:23px">Email</div>
    <div class="field" style="top:67px;height:23px">Subject</div>
    <div class="field" style="top:94px;height:76px">Message</div>
    <div class="send">Send message</div>
  </form>
</section>

<footer class="abs site-footer">
  <div class="footer-col" style="left:81px">
    <h4>Links</h4>
    <ul><li>The Problem</li><li>The Solution</li><li>The Result</li><li>Services</li><li>Projects</li></ul>
  </div>
  <div class="footer-col" style="left:314px">
    <h4>About Us</h4>
    <p style="margin-top:15px;width:160px">Lorem Ipsum is simply dummy text of the printing and typesetting industry. Lorem Ipsum has been the industry's standard dummy text ever since the 1500s,</p>
  </div>
  <div class="footer-col" style="left:607px">
    <h4>Contact Info</h4>
    <ul><li>Torvik AS</li><li>Brekkeveien 58</li><li>1520 Moss</li><li>Norway</li><li>eMail: info@stonebrace.example</li><li>Phone: 1-800-555-0142</li></ul>
  </div>
</footer>
<div class="abs copyright">Copyright 2013 Stonebrace.example</div>
<div class="abs social" aria-label="Social links">
  <span style="background:#3fa9dc"></span><span style="background:#3b5b98"></span><span style="background:#c4302b"></span><span style="background:#d8432f"></span>
</div>

</body>
</html>
```